Corporate Design für Lindmar Naturwerk
Die Desgins sind wunderschön geworden. Die Kommunikation war stets sehr freundlich und schnell. Wir freuen uns auf die auch weiterhin bestehende und Zukünftige Zusammenarbeit.
Zielgruppe
Verkauf von diversen hoch qualitativen Honigprodukten. Produktion eigener Honig Produkte unter der Marke Lindmar Naturwerk.
Online Shop in der Schweiz
Aufgabenstellung
Das Logo soll aus einer Krone mit Gold-Schwarzen Bienen Streifen sein. Das ganze Design soll Bezug zu Honig und Bienen haben.
Wir sind offen für diverse Ideen. (evtl. auch Bezug zu Schweiz)

```html
<!DOCTYPE html>
<html lang="de">
<head>
<meta charset="utf-8">
<title>Lindmar Naturwerk – Geschäftsausstattung</title>
<link href="https://fonts.googleapis.com/css2?family=Jost:wght@400;500&family=Lora:wght@400;600&display=swap" rel="stylesheet">
<style>
  :root {
    --bg: #e7e4df;
    --paper: #ffffff;
    --ink: #1f1f1f;
    --gold: #f2b51e;
    --gold-line: #f5cc6a;
    --rule: #cfcfcf;
  }
  * { margin: 0; padding: 0; box-sizing: border-box; }
  html, body { width: 1200px; height: 1040px; overflow: hidden; }
  body { background: var(--bg); position: relative; font-family: "Jost", sans-serif; color: var(--ink); }

  .sheet { position: absolute; background: var(--paper); box-shadow: 0 2px 10px rgba(0,0,0,.18); }
  .letter { left: 96px; top: 56px; width: 672px; height: 928px; }
  .card-front { left: 833px; top: 56px; width: 268px; height: 415px; }
  .card-back { left: 833px; top: 570px; width: 268px; height: 414px; }

  .pos { position: absolute; }
  .gold-rule { position: absolute; left: 0; right: 0; height: 1px; background: var(--gold-line); }

  .brand { display: flex; align-items: center; gap: 8px; white-space: nowrap; }
  .brand-dot { width: 12px; height: 12px; border-radius: 50%; background: var(--gold); }
  .brand-name { font-family: "Jost", sans-serif; font-weight: 500; color: var(--ink); letter-spacing: .02em; }

  /* letter */
  .letter .brand { right: 64px; top: 125px; }
  .letter .brand-name { font-size: 19px; }
  .sender-line { left: 79px; top: 144px; font-family: "Lora", serif; font-size: 7.5px; }
  .letter .gold-rule { top: 158px; }
  .recipient { left: 79px; top: 172px; font-size: 11px; line-height: 15.2px; }
  .date { right: 64px; top: 264px; font-size: 8.5px; }
  .subject { left: 79px; top: 293px; font-family: "Lora", serif; font-weight: 600; font-size: 10.5px; }
  .body-text { left: 79px; top: 323px; width: 530px; font-size: 10.6px; line-height: 15.2px; }
  .body-text p { margin-bottom: 15.2px; }
  .body-text p.tight { margin-bottom: 0; }
  .signature { left: 77px; top: 710px; width: 80px; height: 22px; background: linear-gradient(90deg, #e6e6e6, #f4f4f4); }
  .signer { left: 79px; top: 732px; font-size: 11px; }
  .footer-rule { position: absolute; left: 0; right: 0; top: 827px; height: 1px; background: var(--rule); }
  .footer-col { top: 837px; font-size: 8.3px; line-height: 12.3px; }
  .col-1 { left: 63px; } .col-2 { left: 208px; } .col-3 { left: 353px; } .col-4 { left: 498px; }

  /* cards */
  .card-front .brand { left: 0; right: 0; top: 325px; justify-content: center; }
  .card-front .brand-name { font-size: 21px; }
  .card-front .gold-rule { top: 367px; }
  .contact { left: 49px; font-size: 13px; line-height: 19px; }
  .contact-name { left: 49px; top: 140px; font-family: "Lora", serif; font-size: 12.5px; }
  .contact-name .sep { color: var(--gold); }
  .address { top: 178px; }
  .phones { top: 236px; }
  .web { top: 293px; }
  .card-back .gold-rule { top: 366px; }
</style>
</head>
<body>
  <section class="sheet letter">
    <div class="pos brand"><span class="brand-dot"></span><span class="brand-name">LINDMAR NATURWERK</span></div>
    <div class="pos sender-line">Max Muster · Musterstraße 1 · 23456 Musterstadt</div>
    <div class="gold-rule"></div>

    <address class="pos recipient" style="font-style:normal">Bernd Beispiel<br>Beispielweg 7<br>89012 Beispielstadt</address>
    <div class="pos date">Musterstadt, TT. Monat JJJJ</div>
    <div class="pos subject">Stet clita kasd gubergren no sea</div>

    <div class="pos body-text">
      <p>Sehr geehrter Herr Beispiel,</p>
      <p>lorem ipsum dolor sit amet, consetetur sadipscing elitr, sed diam nonumy eirmod tempor invidunt ut labore et dolore magna aliquyam erat, sed diam voluptua.</p>
      <p>At vero eos et accusam et justo duo dolores et ea rebum. Stet clita kasd gubergren, no sea takimata sanctus est Lorem ipsum dolor sit amet. Lorem ipsum dolor sit amet, consetetur sadipscing elitr, sed diam nonumy eirmod tempor invidunt ut labore.</p>
      <p class="tight">Dolore magna aliquyam erat, sed diam voluptua. At vero eos et accusam et justo duo dolores et ea rebum. Stet clita kasd gubergren, no sea takimata sanctus est Lorem ipsum dolor sit amet.</p>
      <p class="tight">At vero eos et accusam et justo duo dolores et ea rebum. Stet clita kasd gubergren, no sea takimata sanctus est Lorem ipsum dolor sit amet. Lorem ipsum dolor sit amet, consetetur sadipscing elitr, sed diam nonumy eirmod tempor invidunt ut labore.</p>
      <p>Dolore magna aliquyam erat, sed diam voluptua. At vero eos et accusam et justo duo dolores et ea rebum. Stet clita kasd gubergren, no sea takimata sanctus est Lorem ipsum dolor sit amet. At vero eos et accusam et justo duo dolores et ea rebum. Stet clita kasd gubergren, no sea takimata sanctus est Lorem ipsum dolor sit amet. Lorem ipsum dolor sit amet, consetetur sadipscing elitr, sed diam nonumy eirmod tempor invidunt ut labore.</p>
      <p>Dolore magna aliquyam erat, sed diam voluptua. At vero eos et accusam et justo duo dolores et ea rebum. Stet clita kasd gubergren, no sea takimata sanctus est Lorem ipsum dolor sit amet.</p>
      <p>Mit freundlichen Grüßen,</p>
    </div>
    <div class="pos signature" role="img" aria-label="Handschriftliche Unterschrift"></div>
    <div class="pos signer">Max Muster</div>

    <div class="footer-rule"></div>
    <div class="pos footer-col col-1">Firmenname und Rechtsform<br>Geschäftsführer<br>Musterstraße 1<br>23456 Musterstadt</div>
    <div class="pos footer-col col-2">Telefon 01234 567890<br>Fax 01234 567899<br>muster@muster.de<br>www.muster.de</div>
    <div class="pos footer-col col-3">DE21 1234 5678 0000 0123 45<br>ABCD DE XX XXX<br>Ust-IdNr.<br>HRS-Nummer</div>
    <div class="pos footer-col col-4">CH21 1234 5678 0000 0123 45<br>ABCD CH XX XXX<br>Ust-IdNr.<br>HRS-Nummer</div>
  </section>

  <section class="sheet card-front">
    <div class="pos brand"><span class="brand-dot"></span><span class="brand-name">LINDMAR NATURWERK</span></div>
    <div class="gold-rule"></div>
  </section>

  <section class="sheet card-back">
    <div class="pos contact-name">Max Muster <span class="sep">·</span> Geschäftsführer</div>
    <div class="pos contact address">Musterstraße 1<br>23456 Musterstadt</div>
    <div class="pos contact phones">Telefon 01234 567890<br>Fax 01234 567899</div>
    <div class="pos contact web">mail@muster.de<br>muster@muster.de<br>www.muster.de</div>
    <div class="gold-rule"></div>
  </section>
</body>
</html>
```